Smart Home App Needs 4 Mockup Screens. Extra Work Guaranteed for Winner

BACKGROUND
Our company, Lumora, is launching an exciting new app early next year. And we need some examples of what our app will look like to show to some of the biggest retailers in the world. We hope that this project will lead to regular work as we have a lot of new products planned for the app.

Our app will support baby, home and pet monitors (cameras) as well as the world's first smart pet flap.

The monitors allow you to do much more than just watch live video. By monitoring and providing information on sound, movement and temperature the app provides the user with instant peace of mind wherever they are. If anything has changed the user can be alerted via notifications. If motion is detected the user will receive a clip of the whole event moments after it has happened.

The Smart Pet Flap is packed full of features too. From letting you decide when your pet can or can't go outside from your mobile, to automatically opening if a fire is detected (along with a whole host of other features) - this really is the most advanced pet flap in the world.

REQUIREMENTS
We need 4 mock-up screens creating to show the UI of our app.
1. Camera Home Page
2. Camera Notifications Page
3. Pet Flap Fire Alarm Warning Page
4. Extreme Weather Warning Page

Optional - Happy to Pay the Winner Extra for these Designs
5. Start Up/Log In Page
6. Pet Flap Notification Example
7. Pet Flap Scheduler Page (your choice)
(SEE LUMORA APP DESIGN COMPETITION - ATTACHED)

STYLE GUIDE
As you'll see from our wireframes we want our app to be very minimal and modern. The predominant colour will be white but where colour is used it should be bright (see our colour palette - which we will provide shortly).

INSPIRATION
We love the UI of Finchly (home surveillance). Also check out Vesk (smart thermostat).
(SEE LUMORA UI EXAMPLES ATTACHED)

LOGO
We love our logo. Feel free to use it in creative ways.

So far we're also using it as a kind of beacon to indicate if everything is ok.

LOGO COLOURS & APP COLOURS
As mentioned, we are thinking of using the green logo to indicate that everything is ok (and also for the pet app in general). We reserve red for when something has happened (normally bad) and needs attention, like a fire alarm going off.

The app will be predominantly black and white with the odd minimal flash of colour (probably primary colour)
We'll upload a colour scheme as soon as we have it.

CONTACT
Please message us for more details - we'll do our best to reply promptly.

FUTURE WORK
We will need extra screens made straight after the competition is over and there should be additional regular work after this.

Target Market(s)

Our app will be used by young professionals, to young parents to grandparents. The design must be contemporary but timeless and easy to use no matter how good you are with technology.

Industry/Entity Type

Pet

Font styles to use
Sans Serif

Colors
faee3f
33a6d7
ec1f27
acd036
32b7a4

Requirements
Must have
• Beautiful, minimal design. Make sure you spend time looking at the Finchly and Vesk apps before starting.

For the videos make sure you use sensible images - that you'd expect to see from a monitor (high resolution images if possible)
Nice to have
• Creative use of our logo.
Should not have
• Too much detail/clutter/colours. Ugly fonts.

```html
<!DOCTYPE html>
<html lang="en">
<head>
<meta charset="utf-8">
<title>Lumora – Extreme Weather Warning</title>
<link rel="stylesheet" href="https://fonts.googleapis.com/css2?family=Open+Sans:wght@300;400;600&display=swap">
<style>
  :root {
    --white: #ffffff;
    --ink: #1f1f1f;
    --text: #2b2b2b;
    --sun: #faee3f;
    --storm: #f6ea6a;
    --option-bg: #f5f5f5;
    --divider: #e6e6e6;
  }
  * { box-sizing: border-box; margin: 0; padding: 0; }
  html, body {
    width: 900px;
    height: 1200px;
    overflow: hidden;
    background: var(--white);
  }
  .screen {
    position: relative;
    width: 900px;
    height: 1200px;
    background: var(--white);
    font-family: "Open Sans", sans-serif;
    color: var(--text);
  }
  .status-bar {
    position: absolute;
    top: 0; left: 0; right: 0;
    height: 48px;
    display: flex;
    align-items: center;
    justify-content: space-between;
    padding: 0 22px;
    font-size: 24px;
    font-weight: 400;
    color: var(--ink);
  }
  .status-bar .carrier { display: flex; align-items: center; gap: 8px; }
  .signal { display: flex; gap: 3px; }
  .signal span {
    width: 11px; height: 11px; border-radius: 50%;
    border: 1.5px solid var(--ink);
  }
  .signal span.on { background: var(--ink); }
  .status-bar .time { font-weight: 600; }
  .status-bar .power { display: flex; align-items: center; gap: 10px; }
  .battery {
    width: 46px; height: 20px;
    border: 2px solid var(--ink);
    border-radius: 4px;
    padding: 2px;
    position: relative;
  }
  .battery::before {
    content: ""; display: block; width: 100%; height: 100%;
    background: var(--ink); border-radius: 1px;
  }
  .battery::after {
    content: ""; position: absolute; right: -6px; top: 5px;
    width: 3px; height: 7px; background: var(--ink); border-radius: 0 2px 2px 0;
  }
  .brand {
    position: absolute;
    top: 62px; right: 28px;
    display: flex; align-items: center; gap: 10px;
    font-size: 26px; font-weight: 600;
    color: var(--ink);
  }
  .brand-dot {
    width: 26px; height: 26px; border-radius: 50%;
    background: var(--sun);
  }
  .weather-art {
    position: absolute;
    top: 196px; left: 50%;
    transform: translateX(-50%);
    width: 450px; height: 467px;
    border-radius: 24px;
    background: radial-gradient(ellipse at 50% 40%, #ededed 0%, #f7f7f7 55%, #ffffff 100%);
    display: flex; align-items: flex-end; justify-content: center;
  }
  .weather-art .bolt-tone {
    width: 90px; height: 10px; border-radius: 5px;
    background: var(--storm); margin-bottom: 40px; opacity: .7;
  }
  .alert-message {
    position: absolute;
    top: 740px; left: 0; right: 0;
    text-align: center;
    font-size: 29px;
    font-weight: 300;
    line-height: 36px;
    color: var(--text);
  }
  .options {
    position: absolute;
    top: 920px; left: 0; right: 0;
    list-style: none;
    background: var(--option-bg);
  }
  .options li {
    height: 77px;
    display: flex; align-items: center; justify-content: center;
    font-size: 21px; font-weight: 400;
    color: var(--text);
    border-top: 1px solid var(--divider);
  }
  .options li:first-child { border-top: none; }
</style>
</head>
<body>
  <main class="screen">
    <header class="status-bar">
      <div class="carrier">
        <div class="signal"><span class="on"></span><span class="on"></span><span class="on"></span><span></span><span></span></div>
        <span>KESTREL</span>
        <svg width="24" height="18" viewBox="0 0 24 18" aria-hidden="true">
          <path d="M2 6a15 15 0 0 1 20 0" fill="none" stroke="#1f1f1f" stroke-width="2.4" stroke-linecap="round"/>
          <path d="M6 10a9 9 0 0 1 12 0" fill="none" stroke="#1f1f1f" stroke-width="2.4" stroke-linecap="round"/>
          <circle cx="12" cy="15" r="2.4" fill="#1f1f1f"/>
        </svg>
      </div>
      <div class="time">4:21 PM</div>
      <div class="power">
        <svg width="14" height="22" viewBox="0 0 14 22" aria-hidden="true">
          <path d="M2 6l10 10-5 4V2l5 4L2 16" fill="none" stroke="#555" stroke-width="1.6" stroke-linejoin="round"/>
        </svg>
        <span>100%</span>
        <div class="battery"></div>
      </div>
    </header>

    <div class="brand"><span class="brand-dot"></span>Lumora</div>

    <div class="weather-art" role="img" aria-label="Large thunderstorm icon: dark outlined cloud with slanted rain streaks and a yellow lightning bolt">
      <div class="bolt-tone"></div>
    </div>

    <p class="alert-message">
      A severe thunderstorm is set<br>
      predicted tonight from 11:00 PM - 6:00 AM<br>
      What do you want to do?
    </p>

    <ul class="options">
      <li>Ensure Fido is locked in for the duration.</li>
      <li>Adjust Fido's pet flap schedule</li>
      <li>Ignore for now</li>
    </ul>
  </main>
</body>
</html>
```